Www.zapdeck.com monthly sweepstakes.

Every month I am giving away 1st place $500 gift card to your local RC hobby shop of choice, 2nd place $100 gift card 3rd place ZapDeck merch. All things rc: cars, boats, quadcopters, helicopters, airplanes.

Needs to be with the color theme of the website. Check zapdeck.com for current sweepstakes banner. New banner should be half the size in height. I will post dimension later.

Target Market(s)

Rc hobbies cars airplanes helicopters boats

Industry/Entity Type

RemoteControl hobbies

Requirements
Must have
• 1440x680 size, Blend with black background, creative and in incorporate all trypes of rc craft
Should not have
• To many different colors, dosnt need logo as its already on website. This is a banner for my homepage

```html
<!DOCTYPE html>
<html lang="en">
<head>
<meta charset="utf-8">
<title>ZapDeck Monthly Sweepstakes Banner</title>
<link rel="stylesheet" href="https://fonts.googleapis.com/css2?family=Bebas+Neue&family=Arimo:wght@400;700&display=swap">
<style>
  :root {
    --backdrop: #dedede;
    --ink: #000000;
    --paper: #ffffff;
    --brand-red: #e8000f;
    --photo-sky: #7fa6c9;
  }
  * { margin: 0; padding: 0; box-sizing: border-box; }
  html, body { width: 1200px; height: 649px; overflow: hidden; background: var(--backdrop); }
  .stage { position: relative; width: 1200px; height: 649px; }
  .art { position: absolute; left: 0; top: 0; width: 1200px; height: 649px; }
  .headline {
    position: absolute; left: 660px; width: 420px; text-align: center;
    font-family: "Bebas Neue", "Arial Narrow", sans-serif; line-height: 1;
  }
  .headline--win { top: 114px; font-size: 70px; color: var(--brand-red); letter-spacing: -0.5px; }
  .headline--spree { top: 183px; font-size: 70px; color: var(--ink); letter-spacing: -1.5px; }
  .rule { position: absolute; left: 806px; top: 267px; width: 127px; height: 3px; background: var(--brand-red); }
  .place {
    position: absolute; background: var(--brand-red); color: var(--paper);
    font-family: "Arimo", Arial, sans-serif; font-weight: 700;
    display: flex; align-items: center; justify-content: center; line-height: 1;
  }
  .place sup { font-size: 0.55em; vertical-align: top; position: relative; top: -0.15em; margin-left: 2px; }
  .place--first { left: 648px; top: 305px; width: 115px; height: 68px; font-size: 40px; }
  .place--second { left: 676px; top: 396px; width: 88px; height: 53px; font-size: 30px; }
  .place--third { left: 705px; top: 471px; width: 60px; height: 36px; font-size: 21px; }
  .prize { position: absolute; font-family: "Arimo", Arial, sans-serif; color: var(--ink); line-height: 1; white-space: nowrap; }
  .prize strong { font-weight: 700; }
  .prize--first { left: 780px; top: 301px; font-size: 43px; font-weight: 700; }
  .prize--first-note { left: 781px; top: 348px; font-size: 23px; }
  .prize--second { left: 778px; top: 399px; font-size: 31px; }
  .prize--second strong { font-size: 41px; }
  .prize--third { left: 779px; top: 480px; font-size: 23px; font-weight: 700; }
</style>
</head>
<body>
<div class="stage">
  <svg class="art" viewBox="0 0 1714 927" xmlns="http://www.w3.org/2000/svg">
    <rect class="banner-ground" x="145" y="126" width="1440" height="679" fill="var(--ink)"/>
    <path class="info-panel" d="M1005,126 C860,200 790,330 800,465 C790,600 860,730 1005,805 L1585,805 L1585,126 Z" fill="var(--paper)"/>
    <path class="panel-edge" d="M990,126 C845,200 775,330 785,465 C775,600 845,730 990,805" fill="none" stroke="var(--paper)" stroke-width="2" stroke-dasharray="7 5"/>

    <g class="photo-rings" fill="none" stroke="var(--brand-red)" stroke-width="1.5">
      <circle cx="322" cy="360" r="152"/>
      <circle cx="562" cy="242" r="108"/>
      <circle cx="380" cy="645" r="132"/>
      <circle cx="625" cy="688" r="108"/>
    </g>
    <g class="ring-dots" fill="var(--brand-red)">
      <circle cx="436" cy="254" r="6"/><circle cx="292" cy="508" r="6"/>
      <circle cx="316" cy="525" r="5"/><circle cx="663" cy="208" r="5"/>
      <circle cx="459" cy="272" r="4"/><circle cx="499" cy="699" r="5"/>
      <circle cx="518" cy="692" r="4"/><circle cx="730" cy="710" r="5"/>
    </g>

    <circle cx="642" cy="462" r="240" fill="var(--paper)"/>
    <circle cx="642" cy="462" r="232" fill="url(#jetTone)" role="img" aria-label="Photo of a red RC jet with pilot figure and transmitter on a runway"/>
    <circle cx="322" cy="360" r="142" fill="var(--paper)"/>
    <circle cx="322" cy="360" r="136" fill="url(#shipTone)" role="img" aria-label="Photo of an RC cruise ship model on blue water"/>
    <circle cx="562" cy="242" r="100" fill="var(--paper)"/>
    <circle cx="562" cy="242" r="94" fill="url(#truckTone)" role="img" aria-label="Photo of a red RC pickup truck"/>
    <circle cx="380" cy="645" r="122" fill="var(--paper)"/>
    <circle cx="380" cy="645" r="116" fill="url(#heliTone)" role="img" aria-label="Photo of an RC attack helicopter model"/>
    <circle cx="625" cy="688" r="100" fill="var(--paper)"/>
    <circle cx="625" cy="688" r="94" fill="url(#droneTone)" role="img" aria-label="Photo of a small racing quadcopter on a scale"/>

    <defs>
      <linearGradient id="jetTone" x1="0" y1="0" x2="0" y2="1">
        <stop offset="0" stop-color="#8fb6de"/><stop offset="0.35" stop-color="#9aa38a"/>
        <stop offset="0.5" stop-color="#c8313a"/><stop offset="1" stop-color="#4a4b55"/>
      </linearGradient>
      <linearGradient id="shipTone" x1="0" y1="0" x2="0" y2="1">
        <stop offset="0" stop-color="#cfe3f2"/><stop offset="0.5" stop-color="#e9eef2"/><stop offset="1" stop-color="#2e9bd6"/>
      </linearGradient>
      <linearGradient id="truckTone" x1="0" y1="0" x2="0" y2="1">
        <stop offset="0" stop-color="#e4ddd2"/><stop offset="0.5" stop-color="#c7262a"/><stop offset="1" stop-color="#8c7a6b"/>
      </linearGradient>
      <linearGradient id="heliTone" x1="0" y1="0" x2="0" y2="1">
        <stop offset="0" stop-color="#d8d6d2"/><stop offset="0.5" stop-color="#7a7458"/><stop offset="1" stop-color="#a9a8a2"/>
      </linearGradient>
      <linearGradient id="droneTone" x1="0" y1="0" x2="0" y2="1">
        <stop offset="0" stop-color="#e8e8e6"/><stop offset="0.5" stop-color="#5fa7a3"/><stop offset="1" stop-color="#cfcfcc"/>
      </linearGradient>
    </defs>
  </svg>

  <div class="headline headline--win">WIN AN RC</div>
  <div class="headline headline--spree">SHOPPING SPREE!</div>
  <div class="rule"></div>

  <div class="place place--first">1<sup>st</sup></div>
  <div class="prize prize--first">$500 gift card</div>
  <div class="prize prize--first-note">to your local hobby shop.</div>

  <div class="place place--second">2<sup>nd</sup></div>
  <div class="prize prize--second"><strong>$100</strong> gift card</div>

  <div class="place place--third">3<sup>rd</sup></div>
  <div class="prize prize--third">ZapDeck Merch</div>
</div>
</body>
</html>
```